New Business Card Design for Business Consulting Business

We need a business card design that reflects the simplicity of our business. We partner with our clients to help them deliver change. We are a different kind of business consulting group. We don't just provide you with the theory. We provide you with the leadership and capability to execute change.

Vonduro is a professional services organisation that partners with their clients to lead the execution of strategic process and system improvement initiatives. Vonduro combines hands on delivery with coaching in best practice methodologies and approaches to build their clients capabilities to ensure their ongoing success in project implementations. Vonduro offers business advisory services in Project Management, Business Process Management, Change Management and Business Analytics.

Reason: Hi Designers, Thanks for all of your great designs. There are some really creative and cool ideas. Everyone is really capturing the essence of my business Vonduro. I am extending the deadline for the business card design by 6 days as I need to consult my Marketing colleague who won't be back in Australia until Wednesday. I would like to sit down with them and review all of the best designs. The key themes of the things I have really liked on my first review are: 1) Capturing the company website on the back of the card. 2) Including the company logo on the back of the card too. 3) Including the types of services on the back of the card that the company offers - Project Management - Business Process Management - Change Management - Business Analytics 4) Utilising some images on the back of the card Just so everyone knows the colour palette for the Vonduro company logo is: R: 0 G: 86 B: 162 or C: 97% M: 73% Y: 4% K: 0% Thanks Gareth

Hi Designers,

Thanks for all of your submissions to date.  I am working through each design and will provide feedback on all the great work.

One thing I would like to ask is if you could submit a version that has my academic credentials under or after my name.  I am not a big fan of doing this but as I am in business consulting it does seem to be quite common.

I hold a Bachelor of Commerce (BCom) and a Master of Business Administration (MBA)

Thanks

Gareth

Hi Designers,

Thanks for all of your fantastic designs.  There are some really great designs here for my business.  I am still in the process of reviewing designs and should have this completed by tomorrow.  Some of the things I have learnt from this round of designs are:

1) I prefer to have the card without my academic qualifications

2) I really like cards that have a blue back

3) I prefer to have my name and title either left or right of centre

I hope this helps and I will endeavour to get through all of the designs tomorrow

Cheers

Gareth

Target Market(s)

We target large corporate organisations

Industry/Entity Type

Leadership

Requirements
Must have
• Must have the following business details

Gareth Pilling - Director
Address: Level 7, 82 Harlow Street, Melbourne, Australia, 3000
Phone: +61 3 527 840 213
Fax: +61 3 9214 5037
Email: gareth.pilling@vonduro-example.com.au
LinkedIn: au.linkedin.com/in/garethjpilling/
Twiiter: @garethjpilling
Website: www.vonduro-example.com.au

```html
<!DOCTYPE html>
<html lang="en">
<head>
<meta charset="utf-8">
<title>Vonduro – Business Card</title>
<link rel="stylesheet" href="https://fonts.googleapis.com/css2?family=Roboto:wght@300;400&display=swap">
<style>
  :root {
    --brand-blue: #0d59a5;
    --link-blue: #1f6fc0;
    --ink: #1b1b1b;
    --paper: #ffffff;
    --stage: #ecebe8;
  }
  * { box-sizing: border-box; margin: 0; padding: 0; }
  html, body {
    width: 1200px; height: 900px; overflow: hidden;
    background: var(--stage);
    font-family: "Roboto", Arial, sans-serif;
  }
  .sheet {
    width: 1200px; height: 900px;
    display: flex; align-items: center; justify-content: center; gap: 40px;
  }
  .card {
    position: relative; width: 560px; height: 320px; overflow: hidden;
    box-shadow: 0 6px 18px rgba(0,0,0,.18);
  }

  /* Front */
  .card-front { background: var(--brand-blue); color: var(--paper); }
  .front-logo {
    position: absolute; left: 70px; top: 92px;
    display: flex; flex-direction: column; align-items: flex-end;
  }
  .front-logo .wordmark { font-size: 104px; font-weight: 300; letter-spacing: 2px; line-height: 1; }
  .front-logo .suffix { font-size: 15px; font-weight: 300; letter-spacing: 1px; margin-top: 8px; }

  /* Back */
  .card-back { background: var(--paper); color: var(--ink); }
  .back-sweep { position: absolute; inset: 0; }
  .back-logo {
    position: absolute; left: 34px; top: 24px;
    display: flex; flex-direction: column; align-items: flex-end;
    color: var(--brand-blue);
  }
  .back-logo .wordmark { font-size: 52px; font-weight: 300; letter-spacing: 1px; line-height: 1; }
  .back-logo .suffix { font-size: 9px; letter-spacing: .5px; margin-top: 3px; }
  .holder { position: absolute; left: 34px; top: 100px; }
  .holder-name { font-size: 27px; font-weight: 300; color: var(--brand-blue); line-height: 1.1; }
  .holder-title { font-size: 15px; color: var(--ink); }
  .contact {
    position: absolute; left: 34px; top: 190px;
    font-size: 11.5px; line-height: 1.55; list-style: none;
  }
  .contact .label { color: var(--link-blue); }
  .contact .gap { display: inline-block; width: 14px; }
</style>
</head>
<body>
<main class="sheet">
  <section class="card card-front" aria-label="Card front">
    <div class="front-logo">
      <span class="wordmark">Vonduro</span>
      <span class="suffix">Pty Ltd</span>
    </div>
  </section>

  <section class="card card-back" aria-label="Card back">
    <svg class="back-sweep" width="560" height="320" viewBox="0 0 560 320" aria-hidden="true">
      <path d="M330 0 Q520 90 500 320 L560 320 L560 0 Z" fill="var(--brand-blue)"/>
    </svg>
    <div class="back-logo">
      <span class="wordmark">Vonduro</span>
      <span class="suffix">Pty Ltd</span>
    </div>
    <div class="holder">
      <div class="holder-name">Gareth Pilling</div>
      <div class="holder-title">Director</div>
    </div>
    <ul class="contact">
      <li><span class="label">Address:</span> Level 7, 82 Harlow Street, Melbourne, Australia, 3000</li>
      <li><span class="label">Phone:</span> +61 3 527 840 213<span class="gap"></span><span class="label">Fax:</span> +61 3 9214 5037</li>
      <li><span class="label">Email:</span> gareth.pilling@vonduro-example.com.au<span class="gap"></span><span class="label">Twitter:</span> @garethjpilling</li>
      <li><span class="label">LinkedIn:</span> au.linkedin.com/in/garethjpilling/<span class="gap"></span><span class="label">Website:</span> www.vonduro-example.com.au</li>
    </ul>
  </section>
</main>
</body>
</html>
```